Hello everyone,
I need someone to design a Business Card for my new company. It's called Norvakeep and we give procurement services of Chilean Salmon and Seafood in General. More specifically we are purchasing agents, quality inspectors and we help with general papework and logistics. Maybe in the future can open to some agriculture items such as Meat, Dairy Products and Fruits.
All this focused in international clients that cannot have the support they need when buying items from Chile.
A main concept is reliability.

Thank you in advance.

Esteban.

Target Market(s)

Salmon and Seafood Importers from all world.

Industry/Entity Type

Business

Contact Information for Business Card

The Name: Esteban Ruiz Pardo
My Mobile: +56 9 47316258
My Location: Puerto varas, Chile

Font styles to use
Serif
Sans Serif

Requirements
Must have
• The company name and a logo.
Nice to have
• Some full color on the back side.
Should not have
• No modern shapes. Just a rectangular business card. Remember that has to be accepted by a lot of different cultures, even senior Japanese clients.

```html
<!DOCTYPE html>
<html lang="en">
<head>
<meta charset="utf-8">
<title>Norvakeep Business Card</title>
<link href="https://fonts.googleapis.com/css2?family=Open+Sans:wght@400;600;700&display=swap" rel="stylesheet">
<style>
  :root {
    --page: #ecebe8;
    --white: #ffffff;
    --blue-deep: #174a86;
    --blue-mid: #1f5c9e;
    --blue-light: #3a7cc0;
    --navy-text: #1d3f70;
    --red: #d4314b;
    --grey-text: #3b3b3b;
    --grey-soft: #777777;
    --salmon: #f08a3c;
    --salmon-light: #f7b27a;
  }
  * { box-sizing: border-box; margin: 0; padding: 0; }
  html, body {
    width: 1200px; height: 1023px; overflow: hidden;
    background: var(--page);
    font-family: "Open Sans", Arial, sans-serif;
  }
  .canvas {
    position: relative; width: 1200px; height: 1023px;
  }
  .card {
    position: absolute; left: 180px; width: 840px; height: 480px;
    overflow: hidden; box-shadow: 0 6px 18px rgba(0,0,0,0.18);
  }
  .card--front { top: 16px; background: var(--white); }
  .card--back {
    top: 526px;
    background: linear-gradient(160deg, var(--blue-light) 0%, var(--blue-mid) 45%, var(--blue-deep) 100%);
  }

  /* front */
  .brand { position: absolute; left: 70px; top: 70px; }
  .brand__name {
    display: flex; align-items: center; gap: 18px;
    font-size: 86px; font-weight: 700; color: var(--navy-text); line-height: 1;
    letter-spacing: -1px;
  }
  .brand__mark { width: 34px; height: 34px; background: var(--red); flex: none; }
  .brand__tagline {
    margin-top: 10px; margin-left: 52px;
    font-size: 22px; color: var(--red); letter-spacing: 1px; text-transform: uppercase;
  }
  .person { position: absolute; left: 70px; top: 232px; }
  .person__name {
    font-size: 27px; font-weight: 600; color: var(--grey-text);
    letter-spacing: 1.5px; text-transform: uppercase;
  }
  .person__role {
    margin-top: 2px; font-size: 14px; color: var(--grey-soft);
    letter-spacing: 1.5px; text-transform: uppercase;
  }
  .band {
    position: absolute; left: 0; right: 0; bottom: 0; height: 170px;
    border-top: 4px solid var(--red);
    background: linear-gradient(100deg, var(--blue-light) 0%, var(--blue-mid) 40%, var(--blue-deep) 100%);
    color: var(--white);
  }
  .contacts { position: absolute; left: 70px; top: 30px; list-style: none; }
  .contacts li {
    display: flex; align-items: center; gap: 14px;
    font-size: 22px; line-height: 36px;
  }
  .contacts svg { width: 20px; height: 20px; flex: none; }
  .office { position: absolute; right: 70px; top: 30px; text-align: left; }
  .office__name { font-size: 22px; font-weight: 600; color: var(--red); line-height: 36px; }
  .office__line { font-size: 22px; line-height: 36px; }

  /* back */
  .photo-area {
    position: absolute; left: 0; top: 0; width: 330px; height: 150px;
    border-bottom-right-radius: 150px 150px;
    background: radial-gradient(ellipse at 40% 40%, var(--salmon-light) 0%, var(--salmon) 70%, #d9652a 100%);
  }
  .back-brand { position: absolute; left: 300px; top: 230px; color: var(--white); }
  .back-brand__name { font-size: 90px; font-weight: 700; line-height: 1; letter-spacing: -1px; }
  .back-brand__tagline {
    margin-top: 10px; font-size: 22px; letter-spacing: 1px; text-transform: uppercase;
  }
</style>
</head>
<body>
<main class="canvas">

  <section class="card card--front" aria-label="Business card front">
    <div class="brand">
      <div class="brand__name"><span class="brand__mark"></span>Norvakeep</div>
      <div class="brand__tagline">Chilean Salmon and Seafood</div>
    </div>
    <div class="person">
      <div class="person__name">Esteban Ruiz Pardo</div>
      <div class="person__role">Business Analyst</div>
    </div>
    <div class="band">
      <ul class="contacts">
        <li>
          <svg viewBox="0 0 20 20" aria-hidden="true"><rect x="0" y="0" width="20" height="20" rx="3" fill="#d4314b"/><path d="M6 4h3l1 3-2 1a7 7 0 0 0 4 4l1-2 3 1v3c-6 1-11-4-10-10z" fill="#fff"/></svg>
          +56 9 47316258
        </li>
        <li>
          <svg viewBox="0 0 20 20" aria-hidden="true"><rect x="0" y="0" width="20" height="20" rx="3" fill="#d4314b"/><rect x="4" y="6" width="12" height="8" fill="none" stroke="#fff" stroke-width="1.5"/><path d="M4 6l6 5 6-5" fill="none" stroke="#fff" stroke-width="1.5"/></svg>
          esteban@norvakeep.com
        </li>
        <li>
          <svg viewBox="0 0 20 20" aria-hidden="true"><circle cx="10" cy="10" r="10" fill="#d4314b"/></svg>
          e.ruiz.pardo
        </li>
      </ul>
      <div class="office">
        <div class="office__name">Norvakeep</div>
        <div class="office__line">2215 Calle Los Alerces</div>
        <div class="office__line">Puerto Varas, Chile</div>
      </div>
    </div>
  </section>

  <section class="card card--back" aria-label="Business card back">
    <div class="photo-area" role="img" aria-label="Close-up photograph of a fresh salmon fillet"></div>
    <div class="back-brand">
      <div class="back-brand__name">Norvakeep</div>
      <div class="back-brand__tagline">Chilean Salmon and Seafood</div>
    </div>
  </section>

</main>
</body>
</html>
```